Zielgruppe
Bright Harbor Fellowship Outreach
website not available yet but:
www.BrightHarborFellowshipOutreach.example
Facebook:
https://m.socialpage.example/Bright-Harbor-Fellowship-Outreach-583716204958312/
Aufgabenstellung
Same as the uploaded icon

```html
<!DOCTYPE html>
<html lang="en">
<head>
<meta charset="utf-8">
<title>Bright Harbor Fellowship Outreach – Identity</title>
<link rel="stylesheet" href="https://fonts.googleapis.com/css2?family=Ubuntu+Condensed&display=swap">
<style>
  :root {
    --navy: #0f3183;
    --accent: #1470b5;
    --ink: #1c1c1c;
    --paper: #ffffff;
    --backdrop: #f8f8f8;
    --text-font: "Ubuntu Condensed", sans-serif;
  }
  * { margin: 0; padding: 0; box-sizing: border-box; }
  html, body { width: 806px; height: 1200px; overflow: hidden; background: var(--backdrop); }
  .sheet { position: relative; width: 806px; height: 1200px; font-family: var(--text-font); }

  .brand-mark { position: absolute; border-radius: 50%; }
  .brand-name { position: absolute; left: 0; right: 0; text-align: center; font-family: var(--text-font); font-weight: 400; }

  .hero .brand-mark { left: 343px; top: 52px; width: 116px; height: 116px; background: var(--navy); }
  .hero .brand-name { top: 176px; font-size: 22px; color: var(--ink); }

  .card { position: absolute; box-shadow: 6px 8px 14px rgba(0,0,0,0.18); }
  .card-front { left: 35px; top: 243px; width: 356px; height: 230px; background: var(--paper); }
  .card-front .edge-band { position: absolute; left: 0; top: 0; width: 9px; height: 100%; background: var(--accent); }
  .card-front .brand-mark { left: 137px; top: 10px; width: 80px; height: 80px; background: var(--navy); }
  .card-front .brand-name { top: 97px; padding-left: 9px; font-size: 14px; color: var(--ink); }

  .person { position: absolute; left: 26px; top: 136px; }
  .person-name { font-size: 13px; color: var(--accent); line-height: 16px; }
  .person-role { font-size: 11px; color: var(--ink); line-height: 16px; }

  .contact { position: absolute; left: 154px; top: 136px; list-style: none; }
  .contact li { position: relative; padding-left: 20px; font-size: 10px; line-height: 14px; color: var(--ink); margin-bottom: 2px; }
  .contact li.small { font-size: 8.6px; }
  .contact svg { position: absolute; left: 0; top: 2px; width: 11px; height: 11px; fill: var(--accent); }

  .card-back { left: 417px; top: 245px; width: 353px; height: 229px; background: var(--navy); }
  .card-back .brand-mark { left: 136px; top: 45px; width: 80px; height: 80px; background: var(--paper); }
  .card-back .brand-name { top: 134px; font-size: 15px; color: var(--paper); }
  .card-back .site { position: absolute; left: 0; right: 0; top: 188px; text-align: center; font-size: 11px; letter-spacing: 1.2px; color: var(--paper); }
</style>
</head>
<body>
<main class="sheet">
  <section class="hero">
    <div class="brand-mark"></div>
    <p class="brand-name">Bright Harbor Fellowship Outreach</p>
  </section>

  <article class="card card-front">
    <div class="edge-band"></div>
    <div class="brand-mark"></div>
    <p class="brand-name">Bright Harbor Fellowship Outreach</p>
    <div class="person">
      <p class="person-name">Max Mustermann</p>
      <p class="person-role">Funktion</p>
    </div>
    <ul class="contact">
      <li><svg viewBox="0 0 12 12"><path d="M6 0a4 4 0 0 0-4 4c0 3 4 8 4 8s4-5 4-8a4 4 0 0 0-4-4zm0 5.6A1.6 1.6 0 1 1 6 2.4a1.6 1.6 0 0 1 0 3.2z"/></svg>Musterstr. 108<br>10000 Musterstadt</li>
      <li><svg viewBox="0 0 12 12"><path d="M2.5 0.5l2 2.6-1.2 1.4c.8 1.8 2.2 3.2 4 4l1.4-1.2 2.6 2-1.3 2.2C4.8 11.3.7 7.2.3 1.8z"/></svg>0123 / 456 789 10</li>
      <li class="small"><svg viewBox="0 0 12 12"><path d="M0 2h12v1L6 7 0 3zM0 4.3l6 4 6-4V10H0z"/></svg>mail@brightharborfellowshipoutreach.example</li>
      <li class="small"><svg viewBox="0 0 12 12"><path d="M6 0a6 6 0 1 0 0 12A6 6 0 0 0 6 0zm0 1a5 5 0 0 1 0 10A5 5 0 0 1 6 1zM5.5 1.2C4.2 2.6 3.6 4.2 3.6 6s.6 3.4 1.9 4.8h1C5.2 9.4 4.6 7.8 4.6 6s.6-3.4 1.9-4.8zm1 0c1.3 1.4 1.9 3 1.9 4.8s-.6 3.4-1.9 4.8h-1c1.3-1.4 1.9-3 1.9-4.8S6.8 2.6 5.5 1.2zM1 3.5h10v.8H1zm0 4.2h10v.8H1zM.8 5.6h10.4v.8H.8z"/></svg>www.brightharborfellowshipoutreach.example</li>
    </ul>
  </article>

  <article class="card card-back">
    <div class="brand-mark"></div>
    <p class="brand-name">Bright Harbor Fellowship Outreach</p>
    <p class="site">www.brightharborfellowshipoutreach.example</p>
  </article>
</main>
</body>
</html>
```